Fairbrook's Vacation Rentals Business Card

Multi Million dollar villa rentals in the Dominican Republic.

Industry/Entity Type

Business

Contact Information for Business Card

I am looking for a high-end look around my company name/logo (see attached) on one side incorporating the following info: first and last name, title, address, phone #, email and company website. On the backside I want to add a full color picture of one of our villas (see attached).

```html
<!DOCTYPE html>
<html lang="en">
<head>
<meta charset="utf-8">
<title>Fairbrook's Vacation Rentals – Business Card</title>
<link href="https://fonts.googleapis.com/css2?family=Lato:wght@400;700&display=swap" rel="stylesheet">
<style>
  :root {
    --backdrop: #484848;
    --orange: #f7941d;
    --orange-deep: #f15a24;
    --ink: #231f20;
    --card-dark: #262223;
    --white: #ffffff;
    --muted: #cfcfcf;
    --sky: #6fa3d8;
    --villa: #ece4d6;
    --pool: #1f8fd6;
  }
  * { margin: 0; padding: 0; box-sizing: border-box; }
  html, body { width: 900px; height: 1200px; overflow: hidden; }
  body {
    background: var(--backdrop);
    font-family: 'Lato', sans-serif;
    position: relative;
  }
  .card {
    position: absolute;
    left: 111px;
    width: 684px;
    height: 400px;
    overflow: hidden;
  }
  /* Front */
  .card-front { top: 170px; background: var(--white); }
  .top-bar {
    position: absolute; top: 0; left: 0; width: 100%; height: 29px;
    background: linear-gradient(90deg, var(--orange) 0%, var(--orange) 40%, #7a4a22 62%, var(--ink) 85%);
  }
  .brand {
    position: absolute; top: 29px; left: 0; width: 100%; height: 191px;
    display: flex; align-items: center; justify-content: center; gap: 26px;
  }
  .brand-dot {
    width: 88px; height: 88px; border-radius: 50%;
    background: var(--orange-deep);
    flex: none;
  }
  .brand-name {
    color: var(--ink);
    font-weight: 700;
    line-height: 1;
  }
  .brand-name .line-main { display: block; font-size: 62px; letter-spacing: 1px; }
  .brand-name .line-sub { display: block; font-size: 38px; letter-spacing: 3px; margin-top: 6px; text-transform: uppercase; }
  .info-band {
    position: absolute; top: 220px; left: 0; width: 100%; height: 150px;
    background: var(--card-dark);
  }
  .info-band::before {
    content: ""; position: absolute; top: 6px; left: 0; width: 100%; height: 2px;
    background: var(--white);
  }
  .person {
    position: absolute; right: 359px; top: 54px; text-align: right;
  }
  .person-name { color: var(--white); font-size: 22px; font-weight: 700; letter-spacing: 0.5px; }
  .person-title { color: var(--orange-deep); font-size: 15px; margin-top: 4px; }
  .divider {
    position: absolute; left: 343px; top: 30px; width: 1px; height: 95px;
    background: linear-gradient(180deg, transparent, #8a8a8a 30%, #8a8a8a 70%, transparent);
  }
  .contacts { position: absolute; left: 362px; top: 42px; list-style: none; }
  .contacts li {
    display: flex; align-items: center; gap: 9px;
    color: var(--white); font-size: 15px; height: 24px;
  }
  .icon {
    width: 18px; height: 18px; border-radius: 4px; background: var(--orange-deep);
    display: flex; align-items: center; justify-content: center; flex: none;
  }
  .address-bar {
    position: absolute; bottom: 0; left: 0; width: 100%; height: 30px;
    background: linear-gradient(90deg, var(--orange), var(--orange-deep));
    color: var(--white); font-size: 15px;
    display: flex; align-items: center; justify-content: center;
  }
  /* Back */
  .card-back { top: 646px; background: var(--card-dark); }
  .villa-photo {
    position: absolute; left: 0; top: 59px; width: 100%; height: 282px;
    border-top: 2px solid var(--white); border-bottom: 2px solid var(--white);
    background: linear-gradient(180deg, var(--sky) 0%, #9cc3e6 18%, var(--villa) 30%, var(--villa) 70%, #cfc7b8 80%, var(--pool) 86%, #2aa8ea 100%);
  }
</style>
</head>
<body>
  <section class="card card-front">
    <div class="top-bar"></div>
    <div class="brand">
      <span class="brand-dot"></span>
      <span class="brand-name">
        <span class="line-main">Fairbrook's</span>
        <span class="line-sub">Vacation Rentals</span>
      </span>
    </div>
    <div class="info-band">
      <div class="person">
        <p class="person-name">Marcus Whitfield</p>
        <p class="person-title">Managing Director</p>
      </div>
      <div class="divider"></div>
      <ul class="contacts">
        <li>
          <span class="icon">
            <svg width="12" height="12" viewBox="0 0 24 24"><path fill="#fff" d="M6.6 10.8a15.1 15.1 0 0 0 6.6 6.6l2.2-2.2c.3-.3.7-.4 1-.2 1.1.4 2.3.6 3.6.6.6 0 1 .4 1 1V20c0 .6-.4 1-1 1A17 17 0 0 1 3 4c0-.6.4-1 1-1h3.5c.6 0 1 .4 1 1 0 1.3.2 2.5.6 3.6.1.3 0 .7-.2 1z"/></svg>
          </span>0755-214-390
        </li>
        <li>
          <span class="icon">
            <svg width="12" height="12" viewBox="0 0 24 24"><rect x="2" y="5" width="20" height="14" fill="none" stroke="#fff" stroke-width="2"/><path d="M2 5l10 8 10-8" fill="none" stroke="#fff" stroke-width="2"/></svg>
          </span>m.whitfield@fairbrookvillas.com
        </li>
        <li>
          <span class="icon">
            <svg width="12" height="12" viewBox="0 0 24 24" fill="none" stroke="#fff" stroke-width="2"><circle cx="12" cy="12" r="9"/><ellipse cx="12" cy="12" rx="4" ry="9"/><path d="M3 12h18"/></svg>
          </span>www.fairbrookvillas.com
        </li>
      </ul>
    </div>
    <div class="address-bar">Palm Coast Road 18, 57000 Sosúa</div>
  </section>

  <section class="card card-back">
    <div class="villa-photo" role="img" aria-label="Photo of a white two-storey villa with a red tiled roof, arched veranda, blue sun loungers and a swimming pool in front, framed by palm trees"></div>
  </section>
</body>
</html>
```